Life Coaching and Personal Development Business. Needs Business Card with Logo

We are a Life Coaching and Personal Development Business based in Melbourne, Victoria. We specialise in assisting Individuals who find themselves at cross roads due to career, relationships or just life experiences that are preventing them from having extraordinary lives in happiness, finance or relationships or just being disconnected from a sense of purpose. Our motto is "we help you get there".

Reason: I am awaiting final concepts from a couple of designers

Reason: Deadline passed so now would like to see more options.

Target Market(s)

Individuals who want to move through the cross roads and who are aware that they require help to do so. They are seeking happy, for filing lives through all aspects career, relationships, family and finance

Industry/Entity Type

Finance

Font styles to use
Script

Requirements
Must have
• logo which is representative of moving forward
Business Name: KD Open Horizons
ABN: 5836017294

I do not have a preference with colour but I do not want red orange or green

Should not have
• The card must not be to busy.

```html
<!DOCTYPE html>
<html lang="en">
<head>
<meta charset="utf-8">
<title>KD Open Horizons – Business Card</title>
<link href="https://fonts.googleapis.com/css2?family=Tinos:ital,wght@0,400;1,400&display=swap" rel="stylesheet">
<style>
  :root {
    --backdrop: #000000;
    --paper: #ffffff;
    --brand-blue: #0a4a8b;
    --name-blue: #1d4f8e;
    --ink: #111111;
    --white: #ffffff;
    --rule: #555555;
  }
  * { margin: 0; padding: 0; box-sizing: border-box; }
  html, body {
    width: 889px;
    height: 1200px;
    overflow: hidden;
    background: var(--backdrop);
    font-family: "Tinos", "Times New Roman", serif;
  }
  .sheet { position: relative; width: 889px; height: 1200px; }

  .card { position: absolute; left: 56px; width: 777px; height: 500px; }
  .card--front { top: 74px; background: var(--paper); }
  .card--back { top: 629px; background: var(--brand-blue); }

  .contact-person {
    position: absolute; right: 22px; top: 18px; text-align: left;
  }
  .contact-person__name {
    color: var(--name-blue); font-size: 24px; line-height: 32px;
  }
  .contact-person__phone {
    display: flex; align-items: center; gap: 6px;
    color: var(--ink); font-size: 22px; line-height: 34px;
  }

  .brand-mark {
    position: absolute; left: 190px; top: 214px;
    width: 64px; height: 64px; background: var(--brand-blue);
  }
  .brand-rule {
    position: absolute; left: 295px; top: 210px;
    width: 1px; height: 100px; background: var(--rule);
  }
  .brand-block { position: absolute; left: 320px; top: 220px; }
  .brand-block__name {
    color: var(--name-blue); font-size: 26px; line-height: 30px; letter-spacing: 0.3px;
  }
  .brand-block__abn { color: var(--ink); font-size: 19px; line-height: 26px; }
  .brand-block__tagline {
    color: var(--ink); font-size: 16px; font-style: italic; line-height: 24px; letter-spacing: 0.5px;
  }

  .motto {
    position: absolute; left: 0; right: 0; top: 206px;
    text-align: center; color: var(--white);
    font-size: 55px; font-style: italic; line-height: 64px;
  }
  .back-contact {
    position: absolute; left: 0; right: 0; top: 416px;
    text-align: center; color: var(--white); font-size: 17px; line-height: 25px;
  }
  .back-contact__line { display: flex; justify-content: center; align-items: center; gap: 7px; }
</style>
</head>
<body>
<main class="sheet">
  <section class="card card--front">
    <div class="contact-person">
      <p class="contact-person__name">Natalie Brennan</p>
      <p class="contact-person__phone">
        <svg width="12" height="20" viewBox="0 0 12 20" aria-hidden="true">
          <rect x="1" y="1" width="10" height="18" rx="2" fill="none" stroke="#111" stroke-width="1.6"/>
          <line x1="2" y1="15" x2="10" y2="15" stroke="#111" stroke-width="1.2"/>
        </svg>
        04158 36209
      </p>
    </div>
    <div class="brand-mark"></div>
    <div class="brand-rule"></div>
    <div class="brand-block">
      <p class="brand-block__name">KD OPEN HORIZONS</p>
      <p class="brand-block__abn">ABN: 5836017294</p>
      <p class="brand-block__tagline">Warmth</p>
    </div>
  </section>

  <section class="card card--back">
    <p class="motto">"We help you get there"</p>
    <div class="back-contact">
      <p class="back-contact__line">
        <svg width="16" height="12" viewBox="0 0 16 12" aria-hidden="true">
          <rect x="0.7" y="0.7" width="14.6" height="10.6" fill="none" stroke="#fff" stroke-width="1.2"/>
          <polyline points="0.7,0.7 8,7 15.3,0.7" fill="none" stroke="#fff" stroke-width="1.2"/>
        </svg>
        natb@openhorizons.com.au
      </p>
      <p class="back-contact__line">
        <svg width="11" height="16" viewBox="0 0 11 16" aria-hidden="true">
          <path d="M5.5 0.5C2.7 0.5 0.5 2.7 0.5 5.5c0 3.8 5 10 5 10s5-6.2 5-10C10.5 2.7 8.3 0.5 5.5 0.5z" fill="#fff"/>
          <circle cx="5.5" cy="5.3" r="1.9" fill="#0a4a8b"/>
        </svg>
        P.O. Box 4512, Sandringham VIC 3191
      </p>
    </div>
  </section>
</main>
</body>
</html>
```